Update patient consent forms and contract

Objective
Redesign the existing patient contract information document to create a modern,contempory, and easy-to-understand experience for patients. The updated design should improve readability, accessibility, and overall presentation while maintaining compliance with healthcare and legal requirements.

Key Deliverables

Refreshed visual design and layout
Improved information hierarchy and readability
Modern typography and colour palette aligned with brand guidelines
Clear section headings and navigation
Print-ready and digital versions (PDF)

Include KEV Logo within patient KEV consent to treatment. Ideally this document should be portrait not landscape.
Updates

I would love a front page to be included in the document

```html
<!DOCTYPE html>
<html lang="en">
<head>
<meta charset="utf-8">
<title>Lumen Orthodontics – Treatment Consent Pack</title>
<link href="https://fonts.googleapis.com/css2?family=Poppins:wght@300;400;500;600;700;800&display=swap" rel="stylesheet">
<style>
:root{
  --stage:#8b8b8b;
  --paper:#ffffff;
  --blue:#1a9ad6;
  --ink:#2b2727;
  --text:#3a3a3a;
  --grey:#8d9399;
  --rule:#cfd4d8;
}
*{box-sizing:border-box;margin:0;padding:0}
html,body{width:1200px;height:986px;overflow:hidden}
body{background:var(--stage);font-family:"Poppins",sans-serif;color:var(--text);position:relative}
.sheet{position:absolute;width:550px;height:711px;background:var(--paper);transform:scale(.5676);transform-origin:0 0;overflow:hidden}
.sheet-cover{left:119px;top:83px}
.sheet-retainer{left:444px;top:83px}
.sheet-treatment{left:768px;top:83px}
.sheet-risks{left:281px;top:498px}
.sheet-payment{left:606px;top:498px}

.brand{display:flex;align-items:center;gap:6px;color:var(--grey);font-weight:500}
.brand-dot{width:.75em;height:.75em;border-radius:50%;background:var(--blue);flex:none}

/* cover */
.cover-brand{position:absolute;left:30px;top:72px;font-size:26px}
.cover-title{position:absolute;left:30px;top:188px;font-size:48px;line-height:62px;color:var(--ink);font-weight:400;letter-spacing:.5px}
.cover-title strong{display:block;color:var(--blue);font-weight:800}
.cover-bar{position:absolute;left:31px;top:398px;width:106px;height:6px;background:var(--blue)}
.cover-sub{position:absolute;left:30px;top:440px;font-size:27px;line-height:40px;color:var(--ink);font-weight:300}
.cover-sub b{font-weight:700}
.cover-url{position:absolute;left:232px;top:658px;font-size:8px;color:var(--ink)}

/* shared */
.page-head{display:flex;align-items:center;gap:10px;color:var(--blue);font-weight:600}
.page-head::before,.page-head::after{content:"";flex:1;height:1px;background:var(--rule)}
.section-title{color:var(--blue);font-weight:600;font-size:12px;letter-spacing:.3px}
.item-title{color:var(--blue);font-size:7px;font-weight:400}
.small{font-size:6.4px;line-height:10.3px;text-align:justify}

/* footer */
.page-foot{position:absolute;left:30px;right:30px;top:615px;border-top:1px solid var(--rule);display:grid;grid-template-columns:1fr 1fr 1.1fr;padding-top:6px;font-size:5.2px;line-height:6.4px;color:var(--ink)}
.page-foot>div{padding:0 0 0 0}
.page-foot>div+div{border-left:1px solid var(--rule);padding-left:20px}
.page-foot h4{font-size:7px;font-weight:500;margin-bottom:5px}
.ico-line{display:flex;gap:5px;align-items:flex-start;margin-bottom:5px}
.ico-line svg{width:9px;height:9px;flex:none;stroke:var(--blue);fill:none;stroke-width:1.3}
.ico-line b{font-weight:600}

/* retainer */
.retainer-brand{position:absolute;left:0;right:0;top:52px;justify-content:center;font-size:16px}
.retainer-head{position:absolute;left:30px;right:30px;top:126px;font-size:19px;font-weight:700}
.retainer-body{position:absolute;left:30px;right:30px;top:158px;font-size:10.4px;line-height:20.1px;text-align:justify;color:var(--text)}
.retainer-body em{font-style:normal;color:var(--blue);font-weight:600}

/* treatment */
.art{position:absolute;border-radius:6px}
.art-tooth{left:30px;top:68px;width:120px;height:122px;background:linear-gradient(180deg,#e3f3fb,#c6e6f6)}
.art-hand{left:390px;top:242px;width:110px;height:72px;background:linear-gradient(180deg,#e6f4fb,#cbe8f6)}
.tx-head{position:absolute;left:30px;right:30px;top:24px;font-size:11.5px}
.tx-head::before{flex:.45}
.tx-intro{position:absolute;left:173px;right:30px;top:44px}
.ben-head{position:absolute;left:30px;right:30px;top:226px;font-size:11.5px}
.ben-body{position:absolute;left:30px;width:345px;top:248px}
.risk-rule{position:absolute;left:30px;right:30px;top:328px;height:1px;background:var(--rule)}
.risk-cols{position:absolute;left:30px;right:30px;top:334px;display:grid;grid-template-columns:1fr 1fr;gap:14px}
.risk-cols h3{font-size:11.5px;color:var(--blue);font-weight:600;line-height:14px}
.risk-item{border-top:1px solid #e6e9eb;padding-top:3px;margin-top:3px}
.risk-item:first-child{border-top:0}

/* risks */
.risk-two{position:absolute;left:30px;right:30px;top:12px;display:grid;grid-template-columns:1fr 1fr;gap:14px}
.badge{width:90px;height:22px;border-radius:11px;background:#d7dadd;margin:14px auto 10px}
.sign-line{font-size:6.6px;line-height:10.5px;color:var(--ink);margin:6px 0 0 6px;position:relative}
.sign-line::before{content:"";position:absolute;left:-6px;top:4px;width:2.5px;height:2.5px;border-radius:50%;background:var(--blue)}
.dots{border-bottom:1px dotted #888;height:12px;margin-bottom:8px}
.fill{display:inline-block;border-bottom:1px dotted #888;width:140px}

/* payment */
.pay-title{position:absolute;left:30px;top:26px;font-size:17px;font-weight:700;color:var(--ink)}
.pay-brand{position:absolute;right:30px;top:28px;font-size:11px}
.pay-body{position:absolute;left:30px;right:30px;top:60px;font-size:8.2px;line-height:14.6px;color:var(--ink)}
.pay-body .thanks{font-weight:600;margin-bottom:6px}
.pay-h{color:var(--blue);font-weight:600;font-size:12.5px;margin:12px 0 6px -10px;position:relative;padding-left:10px}
.pay-h::before{content:"";position:absolute;left:0;top:7px;width:3px;height:3px;border-radius:50%;background:var(--blue)}
.pay-sep{height:1px;background:var(--rule);margin-top:10px}
.opt{display:flex;align-items:center;gap:10px;font-weight:600;margin:4px 0 6px}
.box{width:15px;height:15px;border:1.4px solid var(--blue);border-radius:2px}
.opt svg{width:26px;height:24px;stroke:var(--blue);fill:none;stroke-width:1.1;margin-left:14px}
.sig-row{display:flex;justify-content:space-between;font-size:7px;font-weight:600;margin-top:40px}
.pay-addr{position:absolute;left:30px;right:30px;top:587px;border-top:1px solid var(--rule);display:flex;justify-content:space-around;font-size:5.4px;padding-top:5px;color:var(--ink)}
.pay-foot{top:610px}
.bank{display:grid;grid-template-columns:60px 1fr;font-size:5.2px;line-height:8.4px}
.bank span:nth-child(odd){color:var(--blue)}
</style>
</head>
<body>

<!-- Cover -->
<section class="sheet sheet-cover">
  <div class="brand cover-brand"><span class="brand-dot"></span>Lumen Orthodontics</div>
  <h1 class="cover-title">ORTHODONTIC<strong>TREATMENT</strong>CONSENT</h1>
  <div class="cover-bar"></div>
  <p class="cover-sub">Patient Information<br>and <b>Treatment</b><br><b>Agreement</b></p>
  <p class="cover-url">lumen-ortho.example</p>
</section>

<!-- Retainer policy -->
<section class="sheet sheet-retainer">
  <div class="brand retainer-brand"><span class="brand-dot"></span>Lumen Orthodontics</div>
  <h2 class="page-head retainer-head">Our retainer policy</h2>
  <p class="retainer-body">Wearing your retainers is the most important part of your orthodontic journey. Teeth shifting is a part of the natural ageing process just like getting wrinkles, so lifetime maintenance is crucial. Healthy teeth are not meant to be glued together, they are individual units and function independently. This is normally only done for areas of weak bone and gum or damaged teeth. For this reason <em>WE DO NOT ENCOURAGE THE USE OF ‘BONDED’ OR ‘PERMANENT’ RETAINERS.</em> Instead we advocate responsible use of removable retainers to maintain your smile. Permanent or bonded retainers are not actually permanent and can cause other unexpected problems after treatment is completed, such as difficulty to clean around those teeth which can cause plaque trapping and lead to localised gum and bone loss. They are subject to breaking frequently, which is the reason that when bonded retainers are placed, it is recommended that you still wear a removable retainer over them anyway. Bonded retainers only hold the front few teeth, whereas your orthodontic treatment involved improvements of ALL your teeth. Thus, holding the front teeth only gives the back teeth a chance to move out of alignment. The retainers we provide at Lumen Orthodontics, are only worn at night and will hold ALL your teeth where they are at the end of your orthodontic treatment. Even excellent retainer wear will not guarantee that the teeth will stay exactly the same forever, due to the natural ageing and bone changing processes. Minor alignment adjustments may be made to your retainers in the future to ensure that you remain happy with your smile. After 2 years of retainer reviews, further follow up care may be charged at the current office visit rate. Lost or broken retainers will incur a fee for replacement or repair.</p>
  <footer class="page-foot">
    <div><h4>Locations:</h4>
      <p class="ico-line"><svg viewBox="0 0 10 10"><path d="M5 9.3C3 7 2 5.5 2 4a3 3 0 0 1 6 0c0 1.5-1 3-3 5.3z"/><circle cx="5" cy="4" r="1"/></svg><span><b>Fairview</b><br>14 Elm Grove, Fairview VIC 3000</span></p>
      <p class="ico-line"><svg viewBox="0 0 10 10"><path d="M5 9.3C3 7 2 5.5 2 4a3 3 0 0 1 6 0c0 1.5-1 3-3 5.3z"/><circle cx="5" cy="4" r="1"/></svg><span><b>Hillcrest</b><br>8 Ash Lane, Hillcrest VIC 3001</span></p>
      <p class="ico-line"><svg viewBox="0 0 10 10"><path d="M5 9.3C3 7 2 5.5 2 4a3 3 0 0 1 6 0c0 1.5-1 3-3 5.3z"/><circle cx="5" cy="4" r="1"/></svg><span><b>Riverton</b><br>52 Mill Road, Riverton VIC 3002</span></p>
    </div>
    <div><h4>Information:</h4>
      <p class="ico-line"><svg viewBox="0 0 10 10"><path d="M2 1.5h2l1 2.2-1.2.8a5 5 0 0 0 2 2l.8-1.2 2.2 1v2A1 1 0 0 1 7.8 9 7 7 0 0 1 1 2.2a1 1 0 0 1 1-.7z"/></svg><span>03 9000 1234</span></p>
      <p class="ico-line"><svg viewBox="0 0 10 10"><rect x="1.5" y="2.5" width="7" height="5.5" rx="1"/><path d="M3 2.5V1.5h4v1"/></svg><span>03 9000 5678</span></p>
      <p class="ico-line"><svg viewBox="0 0 10 10"><rect x="1" y="2.5" width="8" height="5.5"/><path d="M1 2.5l4 3 4-3"/></svg><span>hello@lumen-ortho.example</span></p>
      <p class="ico-line"><svg viewBox="0 0 10 10"><circle cx="5" cy="5" r="4"/><path d="M1 5h8M5 1c2 2.5 2 5.5 0 8M5 1c-2 2.5-2 5.5 0 8"/></svg><span>lumen-ortho.example</span></p>
    </div>
    <div><h4>Registered Specialist Orthodontists:</h4>
      <p class="ico-line"><svg viewBox="0 0 10 10"><path d="M2 2c1-1 2 0 3 0s2-1 3 0 0 3-.5 4L7 9 5.8 6h-1.6L3 9l-.5-3C2 5 1 3 2 2z"/></svg><span><b>Dr Hanna Reyes</b><br>MDSc, Grad Dip Clin Dent, BDSc(Hons)</span></p>
      <p class="ico-line"><svg viewBox="0 0 10 10"><path d="M2 2c1-1 2 0 3 0s2-1 3 0 0 3-.5 4L7 9 5.8 6h-1.6L3 9l-.5-3C2 5 1 3 2 2z"/></svg><span><b>Dr Tom Varga</b><br>MDSc, Grad Dip Clin Dent, MOrth, BDSc</span></p>
      <p class="ico-line"><svg viewBox="0 0 10 10"><path d="M2 2c1-1 2 0 3 0s2-1 3 0 0 3-.5 4L7 9 5.8 6h-1.6L3 9l-.5-3C2 5 1 3 2 2z"/></svg><span><b>Dr Priya Nair</b><br>DCD, MOrth, MRACDS (Orth), BDSc (Hons)</span></p>
    </div>
  </footer>
</section>

<!-- Orthodontic treatment / benefits / risks -->
<section class="sheet sheet-treatment">
  <h2 class="page-head tx-head">ORTHODONTIC TREATMENT</h2>
  <div class="art art-tooth" role="img" aria-label="Line illustration of a tooth with a brace bracket"></div>
  <p class="small tx-intro">Orthodontic treatment promotes a healthy smile, healthier teeth and gums and a better bite for normal chewing. Orthodontic treatment depends for much of its success on the understanding and co-operation of the patient. This form covers the usual material risks associated with orthodontic treatment. Other factors may also be described by your orthodontist. You may ask your orthodontist to explain anything you do not understand. While recognising the benefits of healthy teeth and a pleasing smile, you should also be aware that orthodontic treatment has limitations and potential risks and there may be alternative treatment options. You should clarify what is expected of you as a patient, or as the parent of a young patient, to achieve excellent results. Keep in mind that with orthodontic treatment, like other healing arts, results cannot be guaranteed. The unknown factor in any orthodontic correction is the response of the patient to the orthodontic treatment. Should you have any questions, please ask. Results depend on care at home, regular visits and wearing appliances exactly as directed by your orthodontist.</p>
  <h2 class="page-head ben-head">BENEFITS</h2>
  <p class="small ben-body">Orthodontics plays an important role in improving overall oral health and achieving balance and harmony between the face and teeth for a healthy smile, which may enhance one's self esteem. Properly aligned teeth and a correct bite promote optimal chewing function and make brushing easier, potentially reducing risk of decay and gum disease. Correctly aligned teeth are less likely to experience abnormal wear. Because of the individual conditions present and the limitations of treatment imposed by nature, each specific benefit may not be attainable for every patient.</p>
  <div class="art art-hand" role="img" aria-label="Line illustration of a hand holding teeth with a gear"></div>
  <div class="risk-rule"></div>
  <div class="risk-cols">
    <div>
      <h3>RISKS</h3>
      <p class="small">All forms of medical and dental treatment, including orthodontics, have some risks and limitations. Fortunately, in orthodontics complications are rare and are usually of a minor consequence if they do occur. Nevertheless, all risks should be considered when making the decision to undergo orthodontic treatment. The principal risks in orthodontic treatment are:</p>
      <div class="risk-item"><p class="item-title">1. Oral Hygiene</p><p class="small">Orthodontic appliances do not cause tooth decay. Gum disease, tooth decay and permanent markings (decalcification) on the teeth can occur if orthodontic patients eat sugary food and drinks or do not brush their teeth frequently or properly. These same problems can occur without orthodontic treatment, but the risk is greater to an individual wearing orthodontic appliances. It is imperative that extra care be taken with oral hygiene during orthodontic treatment.</p></div>
      <div class="risk-item"><p class="item-title">2 Enamel or Restoration Damage</p><p class="small">Minor tooth surface cracks (known as enamel crazing) or, in rare cases, enamel fractures may occur during orthodontics. Damage to the enamel of a tooth or to a restoration (crown, bonding, veneer, etc.) is possible when orthodontic appliances are removed. If the enamel is weaker, the depth of this damage can be deeper and may need restoration. This problem may be more likely when aesthetic (clear or tooth coloured) appliances have been selected. Healthy enamel is less likely to have damage. Your dentist can help if needed.</p></div>
    </div>
    <div>
      <div class="risk-item"><p class="item-title">3 Speech</p><p class="small">Speech can be affected for a short time after appliances are placed. This is more common when there is less room for the tongue. Speech may improve with practice.</p></div>
      <div class="risk-item"><p class="item-title">4 Relapse</p><p class="small">Teeth may tend to change their positions after treatment. The long term, faithful wearing of retainers should reduce this tendency. Teeth can, however, move any time, whether or not they have had orthodontic treatment. This is especially true during the late teen period when active growth of the facial bones is coming to an end. The most vulnerable teeth are those at the front. Throughout life the bite can change adversely from various causes such as eruption of wisdom teeth, growth or maturational changes, mouth breathing, playing of musical instruments and other oral habits. Very occasionally tooth movements will be severe enough to merit a further course of treatment to ensure a satisfactory result.</p></div>
      <div class="risk-item"><p class="item-title">5 Periodontal Health</p><p class="small">The health of the bone and gums which support the teeth may be affected by orthodontic tooth movement if periodontal disease already exists, and in some rare cases where periodontal disease does not appear to exist. Orthodontic treatment may lessen the risk of tooth loss or gum infection due to misalignment of the teeth or jaws. Inflammation of the gums and loss of supporting bone can occur if bacterial plaque is not removed daily with good oral hygiene.</p></div>
    </div>
  </div>
  <footer class="page-foot">
    <div><h4>Locations:</h4>
      <p class="ico-line"><svg viewBox="0 0 10 10"><path d="M5 9.3C3 7 2 5.5 2 4a3 3 0 0 1 6 0c0 1.5-1 3-3 5.3z"/><circle cx="5" cy="4" r="1"/></svg><span><b>Fairview</b><br>14 Elm Grove, Fairview VIC 3000</span></p>
      <p class="ico-line"><svg viewBox="0 0 10 10"><path d="M5 9.3C3 7 2 5.5 2 4a3 3 0 0 1 6 0c0 1.5-1 3-3 5.3z"/><circle cx="5" cy="4" r="1"/></svg><span><b>Hillcrest</b><br>8 Ash Lane, Hillcrest VIC 3001</span></p>
      <p class="ico-line"><svg viewBox="0 0 10 10"><path d="M5 9.3C3 7 2 5.5 2 4a3 3 0 0 1 6 0c0 1.5-1 3-3 5.3z"/><circle cx="5" cy="4" r="1"/></svg><span><b>Riverton</b><br>52 Mill Road, Riverton VIC 3002</span></p>
    </div>
    <div><h4>Information:</h4>
      <p class="ico-line"><svg viewBox="0 0 10 10"><path d="M2 1.5h2l1 2.2-1.2.8a5 5 0 0 0 2 2l.8-1.2 2.2 1v2A1 1 0 0 1 7.8 9 7 7 0 0 1 1 2.2a1 1 0 0 1 1-.7z"/></svg><span>03 9000 1234</span></p>
      <p class="ico-line"><svg viewBox="0 0 10 10"><rect x="1.5" y="2.5" width="7" height="5.5" rx="1"/><path d="M3 2.5V1.5h4v1"/></svg><span>03 9000 5678</span></p>
      <p class="ico-line"><svg viewBox="0 0 10 10"><rect x="1" y="2.5" width="8" height="5.5"/><path d="M1 2.5l4 3 4-3"/></svg><span>hello@lumen-ortho.example</span></p>
      <p class="ico-line"><svg viewBox="0 0 10 10"><circle cx="5" cy="5" r="4"/><path d="M1 5h8M5 1c2 2.5 2 5.5 0 8M5 1c-2 2.5-2 5.5 0 8"/></svg><span>lumen-ortho.example</span></p>
    </div>
    <div><h4>Registered Specialist Orthodontists:</h4>
      <p class="ico-line"><svg viewBox="0 0 10 10"><path d="M2 2c1-1 2 0 3 0s2-1 3 0 0 3-.5 4L7 9 5.8 6h-1.6L3 9l-.5-3C2 5 1 3 2 2z"/></svg><span><b>Dr Hanna Reyes</b><br>MDSc, Grad Dip Clin Dent, BDSc(Hons)</span></p>
      <p class="ico-line"><svg viewBox="0 0 10 10"><path d="M2 2c1-1 2 0 3 0s2-1 3 0 0 3-.5 4L7 9 5.8 6h-1.6L3 9l-.5-3C2 5 1 3 2 2z"/></svg><span><b>Dr Tom Varga</b><br>MDSc, Grad Dip Clin Dent, MOrth, BDSc</span></p>
      <p class="ico-line"><svg viewBox="0 0 10 10"><path d="M2 2c1-1 2 0 3 0s2-1 3 0 0 3-.5 4L7 9 5.8 6h-1.6L3 9l-.5-3C2 5 1 3 2 2z"/></svg><span><b>Dr Priya Nair</b><br>DCD, MOrth, MRACDS (Orth), BDSc (Hons)</span></p>
    </div>
  </footer>
</section>

<!-- Risks continued + authorisation -->
<section class="sheet sheet-risks">
  <div class="risk-two">
    <div>
      <div class="risk-item"><p class="item-title">6 Root Shortening</p><p class="small">In some patients, the length of the roots of the teeth may be shortened during orthodontic treatment. It is nearly impossible to predict patient susceptibility to root shortening. Usually, this shortening does not have significant consequences, but on very rare occasions it may compromise the longevity of the teeth involved.</p></div>
      <div class="risk-item"><p class="item-title">7 Jaw Joints</p><p class="small">Occasionally patients may suffer pain or dysfunction in the jaw joints (TMJ). This may present as joint pain, headaches, or ear problems. These problems may occur with or without orthodontic treatment. Any of the above noted symptoms should be reported to the orthodontist. Some patients are susceptible to TMJ problems, and some are not. Numerous studies have shown that the movement of the teeth during orthodontic treatment is unrelated to the onset of TMJ problems. Just as for painful conditions in other joints, discomfort in TMJ can last from a few days to several weeks or longer.</p></div>
      <div class="risk-item"><p class="item-title">8 Tooth Vitality</p><p class="small">Sometimes a tooth may have been traumatised by a previous accident or a tooth may be decayed or have fillings which can cause damage to the nerve of the tooth. Orthodontic tooth movement may aggravate this condition and in rare instances may lead to loss of tooth vitality and discolouration of the tooth requiring root canal treatment and other dental treatment to restore the colour of the tooth.</p></div>
      <div class="risk-item"><p class="item-title">9 Loose appliances and discomfort</p><p class="small">The gums, cheeks or lips may be scratched or irritated by newly placed appliances or by loose or broken appliances or by trauma to the mouth. You will be given instructions on minimising these effects. Very rarely, loose orthodontic appliances may be accidentally swallowed or aspirated. You should inform your orthodontist of any unusual symptoms, or broken or loose appliances, as soon as they are noted. Usual post-adjustment tenderness or sensitivity of 24-48 hours should be expected, although this can vary with each patient and the procedure performed.</p></div>
      <div class="risk-item"><p class="item-title">10 Atypical Growth</p><p class="small">Insufficient excessive or asymmetrical changes in the growth of the jaws may limit the orthodontist's ability to achieve the desired result. If growth becomes disproportionate during orthodontic management the treatment may be prolonged. Growth changes that occur after orthodontic treatment may alter the quality of treatment results and may require further orthodontic treatment. In some cases of atypical growth, the bite may change so much that oral surgery is required to achieve the best possible result.</p></div>
      <div class="risk-item"><p class="item-title">11 Headgear</p><p class="small">If improperly handled, headgear may cause facial injury. Patients are warned not to wear the appliance during times of boisterous or competitive activity.</p></div>
      <div class="risk-item"><p class="item-title">12 Treatment Time</p><p class="small">The duration of orthodontic treatment can vary depending on factors such as the complexity of the case and patient compliance. Total treatment time may exceed the estimate and delays are more likely with lost or broken appliances, missed appointments, poor cooperation, or unexpected complications.</p></div>
    </div>
    <div>
      <div class="risk-item" style="margin-top:10px"><p class="item-title">13 Co-operation</p><p class="small">Co-operation throughout treatment is your best guarantee of achieving a pleasing smile and a good bite. It is vital to follow your orthodontist's instructions on all aspects of treatment (i.e. wearing elastics, aligners and retainers for the prescribed amount of time). Without your co-operation, treatment may not be as successful. Your orthodontist may need to consider a change in treatment plan or, in rare situations, stop treatment or accept less than ideal results. Best results will occur when you work well with your orthodontist.</p></div>
      <div class="risk-item"><p class="item-title">14 Complementary aesthetic dentistry</p><p class="small">In some situations, achieving the desired aesthetic outcome may require additional dental procedures, such as cosmetic bonding, crowns, or periodontal therapy, to address specific issues not corrected by orthodontic treatment alone.</p></div>
      <div class="risk-item"><p class="item-title">15 General Health</p><p class="small">General medical problems can affect orthodontic treatment. You should keep your orthodontist informed of any changes to your medical health.</p></div>
      <div class="risk-item"><p class="item-title">16 Specific Risks</p><p class="small">Your orthodontist will discuss your case with you in detail and discuss specific risks.</p></div>
      <div class="badge" role="img" aria-label="Professional society membership badge"></div>
      <p class="sign-line">I hereby authorize:</p>
      <div class="dots" style="margin-top:6px"></div>
      <p class="sign-line">to carry out orthodontic treatment and any other related procedures deemed necessary including radiographs, for the welfare and treatment of:</p>
      <div class="dots"></div>
      <p class="sign-line">I confirm that the risks attaching to the proposed treatment have been explained to me by my practitioner and that I fully understand those risks and have determined to proceed with treatment. Signature of patient (or parent/guardian for patients under the age of 18 years):</p>
      <p class="sign-line" style="margin-top:12px">Signature: <span class="fill" style="width:170px"></span></p>
      <p class="sign-line" style="margin-top:12px">Name: <span class="fill" style="width:180px"></span></p>
      <p class="sign-line" style="margin-top:12px">Relationship to patient: <span class="fill" style="width:125px"></span></p>
      <p class="sign-line" style="margin-top:12px">Date: ........... / ..................... / <span class="fill" style="width:95px"></span></p>
      <p class="sign-line" style="margin-top:12px">Signature of Orthodontist: <span class="fill" style="width:118px"></span></p>
    </div>
  </div>
  <footer class="page-foot">
    <div><h4>Locations:</h4>
      <p class="ico-line"><svg viewBox="0 0 10 10"><path d="M5 9.3C3 7 2 5.5 2 4a3 3 0 0 1 6 0c0 1.5-1 3-3 5.3z"/><circle cx="5" cy="4" r="1"/></svg><span><b>Fairview</b><br>14 Elm Grove, Fairview VIC 3000</span></p>
      <p class="ico-line"><svg viewBox="0 0 10 10"><path d="M5 9.3C3 7 2 5.5 2 4a3 3 0 0 1 6 0c0 1.5-1 3-3 5.3z"/><circle cx="5" cy="4" r="1"/></svg><span><b>Hillcrest</b><br>8 Ash Lane, Hillcrest VIC 3001</span></p>
      <p class="ico-line"><svg viewBox="0 0 10 10"><path d="M5 9.3C3 7 2 5.5 2 4a3 3 0 0 1 6 0c0 1.5-1 3-3 5.3z"/><circle cx="5" cy="4" r="1"/></svg><span><b>Riverton</b><br>52 Mill Road, Riverton VIC 3002</span></p>
    </div>
    <div><h4>Information:</h4>
      <p class="ico-line"><svg viewBox="0 0 10 10"><path d="M2 1.5h2l1 2.2-1.2.8a5 5 0 0 0 2 2l.8-1.2 2.2 1v2A1 1 0 0 1 7.8 9 7 7 0 0 1 1 2.2a1 1 0 0 1 1-.7z"/></svg><span>03 9000 1234</span></p>
      <p class="ico-line"><svg viewBox="0 0 10 10"><rect x="1.5" y="2.5" width="7" height="5.5" rx="1"/><path d="M3 2.5V1.5h4v1"/></svg><span>03 9000 5678</span></p>
      <p class="ico-line"><svg viewBox="0 0 10 10"><rect x="1" y="2.5" width="8" height="5.5"/><path d="M1 2.5l4 3 4-3"/></svg><span>hello@lumen-ortho.example</span></p>
      <p class="ico-line"><svg viewBox="0 0 10 10"><circle cx="5" cy="5" r="4"/><path d="M1 5h8M5 1c2 2.5 2 5.5 0 8M5 1c-2 2.5-2 5.5 0 8"/></svg><span>lumen-ortho.example</span></p>
    </div>
    <div><h4>Registered Specialist Orthodontists:</h4>
      <p class="ico-line"><svg viewBox="0 0 10 10"><path d="M2 2c1-1 2 0 3 0s2-1 3 0 0 3-.5 4L7 9 5.8 6h-1.6L3 9l-.5-3C2 5 1 3 2 2z"/></svg><span><b>Dr Hanna Reyes</b><br>MDSc, Grad Dip Clin Dent, BDSc(Hons)</span></p>
      <p class="ico-line"><svg viewBox="0 0 10 10"><path d="M2 2c1-1 2 0 3 0s2-1 3 0 0 3-.5 4L7 9 5.8 6h-1.6L3 9l-.5-3C2 5 1 3 2 2z"/></svg><span><b>Dr Tom Varga</b><br>MDSc, Grad Dip Clin Dent, MOrth, BDSc</span></p>
      <p class="ico-line"><svg viewBox="0 0 10 10"><path d="M2 2c1-1 2 0 3 0s2-1 3 0 0 3-.5 4L7 9 5.8 6h-1.6L3 9l-.5-3C2 5 1 3 2 2z"/></svg><span><b>Dr Priya Nair</b><br>DCD, MOrth, MRACDS (Orth), BDSc (Hons)</span></p>
    </div>
  </footer>
</section>

<!-- Payment option selection -->
<section class="sheet sheet-payment">
  <h2 class="pay-title">Payment Option Selection</h2>
  <div class="brand pay-brand"><span class="brand-dot"></span>Lumen Orthodontics</div>
  <div class="pay-body">
    <p class="thanks">Thank you for choosing Lumen Orthodontics.</p>
    <p>To assist with managing your treatment fees, please select your preferred payment method below. If you would prefer to pay at each scheduled appointment, please advise our reception team. Please note that appointments are generally scheduled every 6–8 weeks.</p>
    <div class="pay-sep"></div>
    <h3 class="pay-h">Please select one option:</h3>
    <div class="opt"><span class="box"></span>Credit Card Direct Debit<svg viewBox="0 0 26 24"><rect x="1" y="3" width="20" height="13" rx="1.5"/><path d="M1 7h20M4 12h6"/><circle cx="20" cy="17" r="5" fill="#fff"/><path d="M17.5 17h5M20.5 15l2 2-2 2"/></svg></div>
    <p>I would like to pay via credit card direct debit.</p>
    <p style="margin-top:8px;line-height:12.2px">I understand that Lumen Orthodontics will send me a secure PayLink payment link to enter my credit card details. The card provided will be securely stored and used as my nominated payment method for future scheduled payments relating to my treatment plan.</p>
    <div class="opt" style="margin-top:18px"><span class="box"></span>Monthly Direct Bank Transfer<svg viewBox="0 0 26 24"><rect x="2" y="3" width="22" height="19" rx="2"/><path d="M7 1v4M19 1v4M8 11h10l-2-2M18 15H8l2 2"/></svg></div>
    <p>I would like to pay via monthly direct bank transfer.</p>
    <p style="margin-top:8px;line-height:12.2px">I understand that I am responsible for ensuring monthly payments are made on time in accordance with my agreed payment arrangement.</p>
    <div class="pay-sep"></div>
    <h3 class="pay-h">Important</h3>
    <p style="line-height:12.2px">When making direct transfer payments, please use the <b>patient's full name</b> as the payment reference (for example: Emily Smith), rather than the account holder's name. This ensures payments are correctly allocated to your treatment account.</p>
    <h3 class="pay-h">Patient Declaration</h3>
    <p style="font-weight:600">I hereby authorise Lumen Orthodontics</p>
    <div class="sig-row"><span>Patient name: ................................</span><span>Signature of Parent: ............................</span><span>Date: .........../.........../..............</span></div>
  </div>
  <div class="pay-addr">
    <span>● 14 Elm Grove, Fairview VIC 3000</span><span>● 8 Ash Lane, Hillcrest VIC 3001</span><span>● 52 Mill Road, Riverton VIC 3002</span>
  </div>
  <footer class="page-foot pay-foot">
    <div><h4>Our bank account details:</h4>
      <div class="bank"><span>Account Name</span><span>: Lumen Orthodontics</span><span>Bank</span><span>: Harbour Bank</span><span>BSB</span><span>: 000 123</span><span>Account Number</span><span>: 12345678</span></div>
    </div>
    <div><h4>Information:</h4>
      <p class="ico-line"><svg viewBox="0 0 10 10"><path d="M2 1.5h2l1 2.2-1.2.8a5 5 0 0 0 2 2l.8-1.2 2.2 1v2A1 1 0 0 1 7.8 9 7 7 0 0 1 1 2.2a1 1 0 0 1 1-.7z"/></svg><span>03 9000 1234</span></p>
      <p class="ico-line"><svg viewBox="0 0 10 10"><rect x="1.5" y="2.5" width="7" height="5.5" rx="1"/><path d="M3 2.5V1.5h4v1"/></svg><span>03 9000 5678</span></p>
      <p class="ico-line"><svg viewBox="0 0 10 10"><rect x="1" y="2.5" width="8" height="5.5"/><path d="M1 2.5l4 3 4-3"/></svg><span>hello@lumen-ortho.example</span></p>
      <p class="ico-line"><svg viewBox="0 0 10 10"><circle cx="5" cy="5" r="4"/><path d="M1 5h8M5 1c2 2.5 2 5.5 0 8M5 1c-2 2.5-2 5.5 0 8"/></svg><span>lumen-ortho.example</span></p>
    </div>
    <div><h4>Registered Specialist Orthodontists:</h4>
      <p class="ico-line"><svg viewBox="0 0 10 10"><path d="M2 2c1-1 2 0 3 0s2-1 3 0 0 3-.5 4L7 9 5.8 6h-1.6L3 9l-.5-3C2 5 1 3 2 2z"/></svg><span><b>Dr Hanna Reyes</b><br>MDSc, Grad Dip Clin Dent, BDSc(Hons)</span></p>
      <p class="ico-line"><svg viewBox="0 0 10 10"><path d="M2 2c1-1 2 0 3 0s2-1 3 0 0 3-.5 4L7 9 5.8 6h-1.6L3 9l-.5-3C2 5 1 3 2 2z"/></svg><span><b>Dr Tom Varga</b><br>MDSc, Grad Dip Clin Dent, MOrth, BDSc</span></p>
      <p class="ico-line"><svg viewBox="0 0 10 10"><path d="M2 2c1-1 2 0 3 0s2-1 3 0 0 3-.5 4L7 9 5.8 6h-1.6L3 9l-.5-3C2 5 1 3 2 2z"/></svg><span><b>Dr Priya Nair</b><br>DCD, MOrth, MRACDS (Orth), BDSc (Hons)</span></p>
    </div>
  </footer>
</section>

</body>
</html>
```